Business card design for a engineering company

I need a double sided business card design for my company "Verdmont Flow Solutions". The card will be used in Malaysia. Sleek and professional, with a little design flare to it.
Information to showcase:
1. Company logo
2. Name, title, phone, email address, website address
3. our products "Pumping technology, Valve & actuation, Air Moving Technology
Example:
Ravi Tanaka
Business manager
ravi.tanaka@verdmont-example.com
www.verdmont-example.com.my
- Pumping technology
- Valve & actuation
- Air moving technology
Target Market(s)
engineers, purchasing managers
Industry/Entity Type
Business
Contact Information for Business Card
Ravi Tanaka
Business manager
ravi.tanaka@verdmont-example.com
www.verdmont-example.com.my
- Pumping technology
- Valve & actuation
- Air moving technology
catch phrase : "Solving flow challenges, exceeding expectations"

```html
<!DOCTYPE html>
<html lang="en">
<head>
<meta charset="utf-8">
<title>Verdmont Flow Solutions – Business Card</title>
<link href="https://fonts.googleapis.com/css2?family=Open+Sans:wght@400;600;700&display=swap" rel="stylesheet">
<style>
  :root {
    --navy: #1f3a4d;
    --text-grey: #3c4a55;
    --orange: #f39020;
    --orange-top: #fbbd1b;
    --orange-bottom: #f3812d;
    --paper: #f7f7f5;
    --backdrop: #e4e2df;
    --white: #ffffff;
  }
  html, body {
    margin: 0;
    padding: 0;
    width: 1200px;
    height: 900px;
    overflow: hidden;
    background: var(--backdrop);
    font-family: "Open Sans", Arial, sans-serif;
  }
  .canvas {
    position: relative;
    width: 1200px;
    height: 900px;
  }
  .card {
    position: absolute;
    top: 300px;
    width: 520px;
    height: 298px;
    box-sizing: border-box;
    border-radius: 3px;
    box-shadow: 0 6px 18px rgba(0,0,0,0.18);
    overflow: hidden;
  }

  /* Front side */
  .card--front {
    left: 50px;
    background: var(--paper);
    color: var(--text-grey);
  }
  .brand {
    position: absolute;
    display: flex;
    align-items: center;
    gap: 12px;
  }
  .brand__dot {
    width: 40px;
    height: 40px;
    border-radius: 50%;
    flex: none;
  }
  .brand__name {
    font-weight: 700;
    line-height: 1.05;
    letter-spacing: 0.02em;
  }
  .card--front .brand {
    top: 52px;
    left: 190px;
  }
  .card--front .brand__dot { background: var(--navy); }
  .card--front .brand__name {
    color: var(--navy);
    font-size: 22px;
  }
  .contact {
    position: absolute;
    left: 34px;
    top: 160px;
    font-size: 13px;
  }
  .contact__name {
    margin: 0;
    font-size: 17px;
    font-weight: 700;
    color: var(--navy);
    letter-spacing: 0.02em;
  }
  .contact__name .surname { color: var(--orange); }
  .contact__title {
    margin: 0 0 10px;
    font-size: 13px;
  }
  .contact__lines {
    display: flex;
    gap: 22px;
    font-size: 12.5px;
  }
  .contact__lines b { color: var(--navy); }
  .tagline {
    position: absolute;
    left: 34px;
    bottom: 26px;
    margin: 0;
    font-size: 19px;
    font-weight: 700;
    color: var(--navy);
    letter-spacing: 0.03em;
  }

  /* Back side */
  .card--back {
    left: 630px;
    background: linear-gradient(160deg, var(--orange-top) 0%, var(--orange) 55%, var(--orange-bottom) 100%);
    color: var(--white);
  }
  .card--back .brand {
    top: 108px;
    left: 0;
    right: 0;
    justify-content: center;
  }
  .card--back .brand__dot {
    width: 52px;
    height: 52px;
    background: var(--white);
  }
  .card--back .brand__name {
    color: var(--white);
    font-size: 28px;
  }
  .products {
    position: absolute;
    left: 28px;
    bottom: 30px;
    margin: 0;
    padding: 0;
    list-style: none;
    display: flex;
    gap: 14px;
    font-size: 13px;
  }
  .products li {
    display: flex;
    align-items: center;
    gap: 6px;
  }
  .products li::before {
    content: "";
    width: 9px;
    height: 9px;
    border-radius: 50%;
    background: var(--white);
  }
</style>
</head>
<body>
<main class="canvas">
  <section class="card card--front" aria-label="Business card front">
    <div class="brand">
      <span class="brand__dot"></span>
      <span class="brand__name">VERDMONT<br>FLOW SOLUTIONS</span>
    </div>
    <div class="contact">
      <p class="contact__name">RAVI <span class="surname">TANAKA</span></p>
      <p class="contact__title">Business manager</p>
      <div class="contact__lines">
        <span><b>P:</b> 98765432</span>
        <span><b>E:</b> ravi.tanaka@verdmont-example.com</span>
      </div>
      <div class="contact__lines" style="margin-top:6px">
        <span><b>www.verdmont-example.com.my</b></span>
      </div>
    </div>
    <p class="tagline">Solving flow challenges, exceeding expectations</p>
  </section>

  <section class="card card--back" aria-label="Business card back">
    <div class="brand">
      <span class="brand__dot"></span>
      <span class="brand__name">VERDMONT<br>FLOW SOLUTIONS</span>
    </div>
    <ul class="products">
      <li>Pumping Technology</li>
      <li>Valve &amp; Actuation</li>
      <li>Air Moving Technology</li>
    </ul>
  </section>
</main>
</body>
</html>
```